Awesome Beer Labels for food pairing

We are going to launch a range of craft beers specially brewed for food pairing, and we are in need of a logo and bottle labels to represent this. Every label individually has to show which beer type it is and the food groups it matches with. At the same time the whole range has to have the same appearance as we are promoting it as a whole package. As we are targeting middle-high to high class hospitality businesses we are looking for a luxurious, exclusive feel to the labels. We also need room for a clear title of the beer and a small food pairing description.

Industry/Entity Type

Craft Brewery

Font styles to use
Sans Serif
Decorative
Script

Colors

Designer to choose colors to be used in the design.

Requirements
Must have
• -Different beer labels where the style and name of the beer comes first, and the beer type second
• - A logo for the whole group which also has to be printed on glasses, so nothing to detailed.
• - Clear, recognizable pictures, drawings or symbols for the different food groups.
• - Room for the name of the beer, the beer type and a small description.
Nice to have
• An exclusive, luxurious look and feel that would not stand out in an high class restaurant.
• Something that combines the whole range of beers (something like a overlaying or connecting picture that combines alle the labels?)
Should not have
• To much different styles, the beers have to match

```html
<!DOCTYPE html>
<html lang="en">
<head>
<meta charset="utf-8">
<title>Craft Brewery Beer Label</title>
<link rel="stylesheet" href="https://fonts.googleapis.com/css2?family=Oswald:wght@400;500;600&family=Roboto+Condensed:wght@400;700&display=swap">
<style>
  :root {
    --backdrop: #f3e4e3;
    --label-black: #252525;
    --rule-grey: #8a8a8a;
    --ornament-light: #c9c9c9;
    --ornament-dark: #6f6f6f;
    --gold: #dba260;
    --gold-deep: #a87a2a;
    --gold-bright: #f2d48a;
    --text-light: #e6e6e6;
    --text-dim: #9a9a9a;
  }
  * { margin: 0; padding: 0; box-sizing: border-box; }
  html, body { width: 1200px; height: 1029px; overflow: hidden; }
  body { background: var(--backdrop); position: relative; }

  .label {
    position: absolute; left: 210px; top: 134px;
    width: 780px; height: 760px;
    background: var(--label-black);
  }
  .label__outer-rule {
    position: absolute; inset: 40px;
    border: 1px solid var(--rule-grey);
  }
  .label__ornament {
    position: absolute; width: 190px; height: 190px;
    background: radial-gradient(circle at 30% 30%, var(--ornament-light), var(--ornament-dark) 55%, transparent 72%);
    opacity: 0.55;
  }
  .label__ornament--tl { left: 28px; top: 28px; }
  .label__ornament--tr { right: 28px; top: 28px; transform: scaleX(-1); }
  .label__ornament--bl { left: 28px; bottom: 28px; transform: scaleY(-1); }
  .label__ornament--br { right: 28px; bottom: 28px; transform: scale(-1,-1); }

  .label__frame {
    position: absolute; left: 180px; top: 175px;
    width: 442px; height: 437px;
    border: 5px solid var(--gold-deep);
    border-image: linear-gradient(135deg, var(--gold-deep), var(--gold-bright) 45%, var(--gold-deep) 70%, var(--gold-bright)) 1;
  }

  .label__est {
    position: absolute; top: 48px;
    font-family: "Oswald", sans-serif; font-weight: 500;
    font-size: 26px; color: var(--text-light); letter-spacing: 1px;
  }
  .label__est--left { left: 86px; }
  .label__est--right { right: 86px; }

  .brand-mark {
    position: absolute; top: 22px; left: 0; right: 0;
    display: flex; flex-direction: column; align-items: center; gap: 4px;
  }
  .brand-mark__dot {
    width: 62px; height: 62px; border-radius: 50%;
    background: var(--gold);
  }
  .brand-mark__name {
    font-family: "Oswald", sans-serif; font-weight: 500;
    font-size: 13px; color: var(--gold); letter-spacing: 2px;
  }

  .label__kicker {
    position: absolute; top: 126px; left: 40px; right: 40px;
    display: flex; align-items: center; gap: 8px;
    font-family: "Roboto Condensed", sans-serif; font-size: 18px;
    color: var(--text-dim); letter-spacing: 1px; white-space: nowrap;
  }
  .label__kicker::before, .label__kicker::after {
    content: ""; flex: 1; height: 1px; background: var(--text-dim);
  }

  .label__title {
    position: absolute; top: 140px; left: 0; right: 0; text-align: center;
    font-family: "Oswald", sans-serif; font-weight: 600;
    font-size: 150px; line-height: 1; color: var(--gold);
    letter-spacing: -2px;
  }

  .label__divider-dot {
    position: absolute; top: 296px; left: 50%; margin-left: -5px;
    width: 10px; height: 10px; border: 1px solid var(--text-dim); border-radius: 50%;
  }
  .label__tagline {
    position: absolute; top: 314px; left: 0; right: 0; text-align: center;
    font-family: "Roboto Condensed", sans-serif; font-weight: 700;
    font-size: 14px; line-height: 1.2; color: var(--text-light); text-transform: uppercase;
  }
  .label__flourish {
    position: absolute; top: 306px; left: 30px; right: 30px; height: 70px;
    background: radial-gradient(ellipse at center, rgba(150,150,150,0.35), transparent 70%);
  }
  .label__fineprint {
    position: absolute; top: 358px; left: 40px; right: 40px; text-align: center;
    font-family: "Roboto Condensed", sans-serif; font-size: 10px; color: var(--text-dim);
  }
  .label__volume {
    position: absolute; bottom: 14px; left: 0; right: 0; text-align: center;
    font-family: "Roboto Condensed", sans-serif; font-size: 19px; color: var(--text-light);
  }
</style>
</head>
<body>
  <main class="label">
    <div class="label__outer-rule"></div>
    <div class="label__ornament label__ornament--tl" role="img" aria-label="Silver baroque scroll ornament"></div>
    <div class="label__ornament label__ornament--tr" role="img" aria-label="Silver baroque scroll ornament"></div>
    <div class="label__ornament label__ornament--bl" role="img" aria-label="Silver baroque scroll ornament"></div>
    <div class="label__ornament label__ornament--br" role="img" aria-label="Silver baroque scroll ornament"></div>

    <section class="label__frame">
      <span class="label__est label__est--left">EST</span>
      <div class="brand-mark">
        <span class="brand-mark__dot"></span>
        <span class="brand-mark__name">OAKHALL</span>
      </div>
      <span class="label__est label__est--right">2018</span>

      <p class="label__kicker">CRAFT BREWERY</p>
      <h1 class="label__title">BEER</h1>

      <div class="label__flourish" role="img" aria-label="Faint grey scroll flourish"></div>
      <span class="label__divider-dot"></span>
      <p class="label__tagline">Lorem ipsum in graphical and<br>textual context</p>
      <p class="label__fineprint">Small batch ale brewed to pair with fine dining.</p>

      <p class="label__volume">Net wt : 160 ml.</p>
    </section>
  </main>
</body>
</html>
```